MaplePilot Dating Plattform Design Proposal

Layout Proposal
HTML or PSD

Dating Platform, where young ladies (f.e. students) are looking for generous man that support them. In return they will spend time with the sugar daddies (dining, cinema, exhibitions, romantic rendez-vous).

Page consist out of 2 pages
1. Primary landing page
2. Detail page for each profile

1. Primary Landing Page
a. Headline: Hier suchen JUNGE FRAUEN, den REIFEN MANN der weiss wie zu verwöhnen!
b. Subtitle/Explanation (can be positioned on top of profiles or at side): Viele junge Frauen können nichts mit den Männern in ihrem Alter anfangen oder sie lieben einfach die Möglichkeiten die ihnen ein reiferer Mann bieten kann. Auf Mapplepilot bieten wir den jungen Damen dafür eine Kontaktmöglichkeit. Sie inserieren auf Maplpilot privat und sind keine profesionellen.
c. List of Profiles with pictures, description text, name and number
2. Detail Page
a. Picture of Profile
b. Description Text
c. Additional blurred pictures
d. Field to enter email to see pictures unblurred

Example pages:
- http://nachtfalter-plauschwelt.ch/

Design:
- Feel free for your suggestions of look’n’feel. Keep in mind that we address generous man
- The way how profiles (20 -30 total) shall be listed on Page 1 is up to you (list, carroussel, slider,..)
- As well feel free to add any background pics/aminations

Attached find Excel with profiles and ZIP with pictures

Dating

2 page

• Page consist out of 2 pages
• 1. Primary landing page
• 2. Detail page for each profile
• 1. Primary Landing Page
• a. Headline: Hier suchen JUNGE FRAUEN, den REIFEN MANN der weiss wie zu verwöhnen!
• b. Subtitle/Explanation (can be positioned on top of profiles or at side): Viele junge Frauen können nichts mit den Männern in ihrem Alter anfangen oder sie lieben einfach die Möglichkeiten die ihnen ein reiferer Mann bieten kann. Auf Mapplepilot bieten wir den jungen Damen dafür eine Kontaktmöglichkeit. Sie inserieren auf Maplpilot privat und sind keine profesionellen.
• c. List of Profiles with pictures, description text, name and number
• 2. Detail Page
• a. Picture of Profile
• b. Description Text
• c. Additional blurred pictures
• d. Field to enter email to see pictures unblurred

```html
<!DOCTYPE html>
<html lang="de">
<head>
<meta charset="utf-8">
<title>MaplePilot – Junge Frauen suchen den reifen Mann</title>
<link rel="stylesheet" href="https://fonts.googleapis.com/css2?family=Open+Sans:wght@400;600&family=Arimo:wght@400&display=swap">
<style>
:root{
  --magenta:#d1165e;
  --card-pink:#c9175c;
  --band:#474747;
  --paper:#ffffff;
  --card-grey:#efefef;
  --button:#2c2c2c;
  --text:#3a3a3a;
  --muted:#5a5a5a;
  --rule:#e2e2e2;
}
*{box-sizing:border-box;margin:0;padding:0}
html,body{width:1200px;height:2258px;overflow:hidden;background:var(--paper)}
body{position:relative;font-family:"Open Sans",Arial,sans-serif;color:var(--text)}

.headline-top{height:68px;display:flex;align-items:center;justify-content:center;
  color:var(--magenta);font-size:36px;font-weight:400;letter-spacing:.3px;white-space:pre}
.hero-band{position:absolute;top:68px;left:0;width:1200px;height:260px;background:var(--band)}
.hero-photo{position:absolute;top:21px;width:167px;height:220px;border:4px solid #fff}
.headline-bottom{position:absolute;top:340px;left:0;width:1200px;text-align:center;
  color:var(--magenta);font-size:38px;font-weight:400}
.intro{position:absolute;top:418px;left:128px;width:944px;text-align:center;
  font-size:17px;line-height:23px;color:var(--muted);letter-spacing:.3px}
.rule{position:absolute;left:0;width:1200px;height:1px;background:var(--rule)}
.cantons{position:absolute;top:524px;left:124px;display:flex;gap:11.8px}
.canton{width:25px;height:29px;border-radius:2px 2px 12px 12px}
.search{position:absolute;top:577px;left:419px;width:383px;height:51px;background:#333;
  border-radius:4px;padding:6px 7px}
.search-field{width:100%;height:100%;background:#fff;border-radius:2px;display:flex;
  align-items:center;justify-content:space-between;padding:0 10px 0 12px;
  font-size:13px;color:#666}

.profiles{position:absolute;top:673px;left:50px;display:flex;gap:24px;align-items:flex-start}
.column{width:257px;display:flex;flex-direction:column;gap:21px}
.profile-card{width:257px;font-family:"Arimo",Arial,sans-serif}
.profile-head{background:var(--card-pink);padding:0 17px 11px}
.profile-title{height:44px;display:flex;justify-content:space-between;align-items:center;color:#fff}
.profile-name{font-family:"Open Sans",Arial,sans-serif;font-size:24px}
.profile-age{font-family:"Open Sans",Arial,sans-serif;font-size:19px}
.profile-photo{width:226px;height:190px;border:3px solid #fff;margin:0 -2px}
.profile-text{background:var(--card-grey);padding:14px 18px 8px;font-size:13.5px;line-height:18px;
  color:#333;hyphens:auto;-webkit-hyphens:auto}
.profile-lines{display:block;overflow:hidden;height:calc(var(--lines) * 18px)}
.continue{height:30px;background:var(--button);color:#fff;font-size:14px;
  display:flex;align-items:center;justify-content:center;letter-spacing:.3px}

.footer{position:absolute;left:0;bottom:0;width:1200px;height:74px;background:var(--band);
  color:#fff;font-size:13px;display:flex;align-items:center;justify-content:center}
</style>
</head>
<body>

<h1 class="headline-top">Hier suchen  JUNGE FRAUEN, den REIFEN</h1>

<section class="hero-band">
  <div class="hero-photo" style="left:51px;background:linear-gradient(160deg,#6d5448,#c2a07f 55%,#d8b43a)" role="img" aria-label="Profilfoto einer jungen Frau"></div>
  <div class="hero-photo" style="left:238px;background:linear-gradient(160deg,#3b2a26,#c89a80 55%,#2a2020)" role="img" aria-label="Profilfoto einer jungen Frau"></div>
  <div class="hero-photo" style="left:425px;background:linear-gradient(160deg,#8a7a70,#d3b59c 50%,#4a3c42)" role="img" aria-label="Profilfoto einer jungen Frau"></div>
  <div class="hero-photo" style="left:612px;background:linear-gradient(160deg,#6a5a52,#8c5e46 50%,#2a2224)" role="img" aria-label="Profilfoto einer jungen Frau"></div>
  <div class="hero-photo" style="left:799px;background:linear-gradient(160deg,#c79e86,#e4d2c4 50%,#8c6a60)" role="img" aria-label="Profilfoto einer jungen Frau"></div>
  <div class="hero-photo" style="left:986px;background:linear-gradient(160deg,#bfb6ad,#9c7c6a 50%,#2a2a2a)" role="img" aria-label="Profilfoto einer jungen Frau"></div>
</section>

<h2 class="headline-bottom">MANN der weiss wie zu verwöhnen!</h2>

<p class="intro">Viele junge Frauen können nichts mit den Männern in ihrem Alter anfangen oder sie lieben einfach die Möglich-keiten die ihnen ein reiferer Mann bieten kann. Auf Mapplepilot bieten wir den jungen Damen dafür eine Kon-taktmöglichkeit. Sie inserieren auf Maplpilot privat und sind keine profesionellen.</p>

<div class="rule" style="top:500px"></div>

<nav class="cantons" role="img" aria-label="Kantonswappen der Schweiz">
  <span class="canton" style="background:#1f4a9a"></span>
  <span class="canton" style="background:#222"></span>
  <span class="canton" style="background:#333"></span>
  <span class="canton" style="background:#c8102e"></span>
  <span class="canton" style="background:#d52b1e"></span>
  <span class="canton" style="background:#1a1a1a"></span>
  <span class="canton" style="background:#d8a010"></span>
  <span class="canton" style="background:#c81e1e"></span>
  <span class="canton" style="background:#3a6ab8"></span>
  <span class="canton" style="background:#d03a3a"></span>
  <span class="canton" style="background:#3b6fcf"></span>
  <span class="canton" style="background:#2e8a3e"></span>
  <span class="canton" style="background:#cc2222"></span>
  <span class="canton" style="background:#c42020"></span>
  <span class="canton" style="background:#f0c400"></span>
  <span class="canton" style="background:#e02626"></span>
  <span class="canton" style="background:#e33030"></span>
  <span class="canton" style="background:#2c9a48"></span>
  <span class="canton" style="background:#2b62c8"></span>
  <span class="canton" style="background:#9ac43a"></span>
  <span class="canton" style="background:#e8b800"></span>
  <span class="canton" style="background:#8cc152"></span>
  <span class="canton" style="background:#d22b2b"></span>
  <span class="canton" style="background:#6fa8e8"></span>
  <span class="canton" style="background:#2a70c8"></span>
</nav>

<div class="search">
  <div class="search-field">
    <span>Search Here Now</span>
    <svg width="22" height="22" viewBox="0 0 22 22" aria-hidden="true"><circle cx="9" cy="9" r="6.5" fill="none" stroke="#d1165e" stroke-width="2.5"/><line x1="14" y1="14" x2="20" y2="20" stroke="#d1165e" stroke-width="2.8" stroke-linecap="round"/></svg>
  </div>
</div>

<div class="rule" style="top:654px"></div>

<main class="profiles">
  <div class="column">
    <article class="profile-card">
      <div class="profile-head"><div class="profile-title"><span class="profile-name">Becky</span><span class="profile-age">30</span></div>
        <div class="profile-photo" style="background:linear-gradient(160deg,#8c7a70,#d2b09a 55%,#9aa8b8)" role="img" aria-label="Profilfoto von Becky"></div></div>
      <p class="profile-text"><span class="profile-lines" style="--lines:12">Habe genug von meinen unreifen Mitstudenten! Ich wünsche mir einen reifen, grosszügigen, verständnisvollen Mann mit einem grossen Herz. Bin eine Studentin, mit knappem Taschengeld. Träume von entspannenden Abenden bei gutem Essen. Wenn du mir meinen Traum erfüllst, versichere ich dir meine Dankbarkeit. Bitte nicht schüchtern sein, bin der</span></p>
      <div class="continue">CONTINUE</div>
    </article>
    <article class="profile-card">
      <div class="profile-head"><div class="profile-title"><span class="profile-name">Emilia</span><span class="profile-age">30</span></div>
        <div class="profile-photo" style="background:linear-gradient(160deg,#c8a878,#8a5a40 55%,#2a2426)" role="img" aria-label="Profilfoto von Emilia"></div></div>
      <p class="profile-text"><span class="profile-lines" style="--lines:8">Suche den älteren charmanten Mann der die Frauen liebt: Junge Männer wissen einfach nicht wie man mich verwöhnt. Die wollen immer nur in den Ausgang, und nicht wie ich in Ausstellungen. Ich liebe ruhige, gemütliche Abende wo viel Zeit für.</span></p>
      <div class="continue">CONTINUE</div>
    </article>
    <article class="profile-card">
      <div class="profile-head"><div class="profile-title"><span class="profile-name">Marion</span><span class="profile-age">30</span></div>
        <div class="profile-photo" style="background:linear-gradient(160deg,#e8c870,#b0704a 55%,#4a3028)" role="img" aria-label="Profilfoto von Marion"></div></div>
      <p class="profile-text"><span class="profile-lines" style="--lines:11">Sehne mich nach einem Geniesser der alten Schule.Mag es wenn man mir die Türe öffnet. Ein Arrangement auf lange Zeit, etwas Liebe, Romanze und Aufregung. Ich bin ein easy going Mädchen mit viel Takt Gefühl und einem natürlichen Bedürfniss nach Erotik. Bist du der Mann meiner Sehnsucht? Lass es uns herausfinden!</span></p>
      <div class="continue">CONTINUE</div>
    </article>
  </div>

  <div class="column">
    <article class="profile-card">
      <div class="profile-head"><div class="profile-title"><span class="profile-name">Brenda</span><span class="profile-age">30</span></div>
        <div class="profile-photo" style="background:linear-gradient(160deg,#2a2024,#8a6058 55%,#3a2c30)" role="img" aria-label="Profilfoto von Brenda"></div></div>
      <p class="profile-text"><span class="profile-lines" style="--lines:9">Kerzenschein, ein Glas Burgunder und sanfter Jazz im Hintergrund, so stell ich mir einen gelungenen Abend an der Seite eines Mannes vor. Dies kann mir kein Mann in meinem Alter bieten. Ich brauche einen Mann, zu dem ich aufsehen kann. Erotisch und materiell können junge Männer meine</span></p>
      <div class="continue">CONTINUE</div>
    </article>
    <article class="profile-card">
      <div class="profile-head"><div class="profile-title"><span class="profile-name">Gina</span><span class="profile-age">30</span></div>
        <div class="profile-photo" style="background:linear-gradient(160deg,#6a5a56,#9a6a52 55%,#d8d4d0)" role="img" aria-label="Profilfoto von Gina"></div></div>
      <p class="profile-text"><span class="profile-lines" style="--lines:7">Gina, Model und Künstlerin: Suche einen grosszügigen, aufmerksamen und reiferen Herr, für gelegentliche Altagsfluchten. Mich stört es nicht wenn du ein Bauch hast, wichtig ist mir, dass du mich verwöhnst und wie eine Dame behandelst.</span></p>
      <div class="continue">CONTINUE</div>
    </article>
    <article class="profile-card">
      <div class="profile-head"><div class="profile-title"><span class="profile-name">Sara</span><span class="profile-age">30</span></div>
        <div class="profile-photo" style="background:linear-gradient(160deg,#e0b890,#c08a68 55%,#8a5a44)" role="img" aria-label="Profilfoto von Sara"></div></div>
      <p class="profile-text"><span class="profile-lines" style="--lines:8">Bitte nur lesen wenn du über 30 Jahre alt bist. Bist du wie ich auf der Suche nach einer lockeren Beziehung in welcher du deine Erfahrung an eine jüngere Frau weitergeben kannst, bei welcher beide Seiten Ihren Genuss daraus ziehen können und</span></p>
      <div class="continue">CONTINUE</div>
    </article>
  </div>

  <div class="column">
    <article class="profile-card">
      <div class="profile-head"><div class="profile-title"><span class="profile-name">Carla</span><span class="profile-age">30</span></div>
        <div class="profile-photo" style="background:linear-gradient(160deg,#c84a30,#e8c0a8 55%,#b81c2a)" role="img" aria-label="Profilfoto von Carla"></div></div>
      <p class="profile-text"><span class="profile-lines" style="--lines:9">Heissblütiger Rotschopf sucht: Meine Eltern sind sehr liebevoll, doch auch ein wenig unorganisiert, darum finanziere ich mein Philosophie Studium alleine. Über Eine Prise Luxus abundzu würde ich mich darum sehr dankbar zeigen. Welcher Mann hat ein grosses Herz für eine Studentin. EInfach eine</span></p>
      <div class="continue">CONTINUE</div>
    </article>
    <article class="profile-card">
      <div class="profile-head"><div class="profile-title"><span class="profile-name">Lara</span><span class="profile-age">30</span></div>
        <div class="profile-photo" style="background:linear-gradient(160deg,#5a4030,#d8c8b0 50%,#8a1c24)" role="img" aria-label="Profilfoto von Lara"></div></div>
      <p class="profile-text"><span class="profile-lines" style="--lines:8">Coifeusse aus Zürich: Habe mich hier angemeldet um Männer kennenzulernen welche schon Lebenserfahrung haben. Mir gefällt es wenn ein Mann einen gewissen Erfahrungsschatz hat und auch weiss wie man eine Dame ausführt und verwöhnt.</span></p>
      <div class="continue">CONTINUE</div>
    </article>
    <article class="profile-card">
      <div class="profile-head"><div class="profile-title"><span class="profile-name">Suze</span><span class="profile-age">30</span></div>
        <div class="profile-photo" style="background:linear-gradient(160deg,#c8b090,#d88a9a 55%,#6a5a50)" role="img" aria-label="Profilfoto von Suze"></div></div>
      <p class="profile-text"><span class="profile-lines" style="--lines:5">Tänzerin liebt Tagträume: Was gibt es Schöneres als mit einem gepflegten Mann gemeinsam Champagner zu trinken?! Den gleichaltrigen Männern fehlt</span></p>
      <div class="continue">CONTINUE</div>
    </article>
  </div>

  <div class="column">
    <article class="profile-card">
      <div class="profile-head"><div class="profile-title"><span class="profile-name">Celine</span><span class="profile-age">30</span></div>
        <div class="profile-photo" style="background:linear-gradient(160deg,#8a7a70,#d0b8a8 50%,#5a4a48)" role="img" aria-label="Profilfoto von Celine"></div></div>
      <p class="profile-text"><span class="profile-lines" style="--lines:9">Art-Studentin: Liebe es mit meiner jugendlichen Frische, Fröhlichkeit und Lernlust dich aufzuheitern. Sich an mir zu laben ist ein Jungbrunnen für Geist und Körper. Wenn du dich dafür erkenntlich zeigst, würde dies mein Herz erwärmen. Wohne alleine und habe viel Zeit. Nun liegt es an dir den nächsten Schritt zu</span></p>
      <div class="continue">CONTINUE</div>
    </article>
    <article class="profile-card">
      <div class="profile-head"><div class="profile-title"><span class="profile-name">Loraine</span><span class="profile-age">30</span></div>
        <div class="profile-photo" style="background:linear-gradient(160deg,#8a7a68,#d8b898 55%,#a88a70)" role="img" aria-label="Profilfoto von Loraine"></div></div>
      <p class="profile-text"><span class="profile-lines" style="--lines:6">Mein lieber Gentleman, befinde mich momentan in einer Situation, in der ich auf die Hilfe und Unterstützung eines Mannes angewiesenbin. Bist du der diskrete Geniesser, der dafür</span></p>
      <div class="continue">CONTINUE</div>
    </article>
    <article class="profile-card">
      <div class="profile-head"><div class="profile-title"><span class="profile-name">Tanja</span><span class="profile-age">30</span></div>
        <div class="profile-photo" style="background:linear-gradient(160deg,#d8d8d8,#8a8a8a 55%,#3a3a3a)" role="img" aria-label="Profilfoto von Tanja in Schwarzweiss"></div></div>
      <p class="profile-text"><span class="profile-lines" style="--lines:11">Sehne mich nach einem Geniesser der alten Schule.Mag es wenn man mir die Türe öffnet. Ein Arrangement auf lange Zeit, etwas Liebe, Romanze und Aufregung. Ich bin ein easy going Mädchen mit viel Takt Gefühl und einem natürlichen Bedürfniss nach Erotik. Bist du der Mann meiner Sehnsucht? Lass es uns herausfinden!</span></p>
      <div class="continue">CONTINUE</div>
    </article>
  </div>
</main>

<footer class="footer">© 2016maplepilotdating.com</footer>

</body>
</html>
```